****FLYER design - LAW FIRM ADVERTISEMENT****

We are a small law firm based in Los Angeles, CA. We need an flyer used for advertising that we will be passing out. We want the flyer to be about 4in x 6in.

We want the flyer to advertise the name of our firm: MARVELLO QUINTARD LLP (no period)
- We want our group photo to take up a good portion of the flyer (although it's okay if parts of the photo have wording over it.)

COLORS: Our firm colors are different shades of steal/metal grey with a bit of a bold orange accent. Any bold writing, like our slogan, names of practice areas,... should be in orange.

We envision a horizontal lay-out of the flyer, but are open to creative options laid out vertically!

Feel free to play with the fonts, the sizing, the color combinations,...

We want the flyer to advertise our two areas of practice: PERSONAL INJURY and EMPLOYMENT LAW. Please also place each photo icon of our areas of practice somewhere around the name (ambulance photo for personal injury; person behind computer desk for employment law). The icons can be relatively small.

Under Personal Injury, please write:
If you or a loved one are suffering from an injury or wrongful death caused by the careless or intentional acts of others, then you have the right to pursue compensation for your injury, out-of-pocket expenses, lost wages, emotional anguish, and more.

Under Employment Law, please write:
Our attorneys regularly represent clients in disputes involving sex, age and race discrimination, sexual harassment, retaliatory discharge, defamation, unlawful termination, breach of employment contracts, and more.

Somewhere on the flyer, please write our slogan IN ITALICS (and probably in orange):
- You Speak. We Listen. They Pay.

In somewhat bright and bold writing, please write "CONTACT US FOR A FREE CONSULTATION TODAY!" (maybe just after our slogan?)
- And under that phrase, write:
- 752 W. Folbrook Lane, Suite 400 Beverly Hills, CA 90210
phone: 310.555.8143
fax: 310.555.9261
email: info@mqmlegal.example
web: www.mqmlegal.example

If possible, and only if there's room without it looking too busy, somewhere in the upper left corner, place our "MQM" logo.
Updates

PLEASE NOTE THAT WE CHANGED OUR GROUP PHOTO TO A SLIGHTLY EDITED ONE.  PLEASE BE SURE TO USE THE NEW ONE!!!  (We deleted the old.)

Target Market(s)

employees, lower and mid-income individuals, minority communities. However, we still want the flyer to look sleek, modern, and professional.

Industry/Entity Type

Advertising

Requirements
Must have
• Firm Name,
Photo of Partners,
Names, photos, and small description of practice areas,
Firm slogan,
"Contact us for a free consultation today!",
Firm contact info.

And only if space and overall look permits, firm "MQM" logo.

We want an overall very sleek, modern feel to our flyer. While we do want to look professional, we wanted a more approachable feel than the typical, conservative law offices.
Nice to have
• Firm "MQM" logo

Horizontal lay out, though we're open to vertical options.

```html
<!DOCTYPE html>
<html lang="en">
<head>
<meta charset="utf-8">
<title>Marvello Quintard LLP – Flyer</title>
<link rel="stylesheet" href="https://fonts.googleapis.com/css2?family=PT+Sans:wght@400;700&family=EB+Garamond:ital@1&display=swap">
<style>
  :root{
    --page:#e9e9ea;
    --steel-light:#c9cacc;
    --steel-mid:#8c8d90;
    --steel-dark:#3a3a3c;
    --ink:#1b1b1c;
    --slate:#5b6570;
    --orange:#f0612a;
    --orange-deep:#d9491a;
    --white:#ffffff;
    --panel:rgba(30,30,31,.72);
  }
  *{box-sizing:border-box;margin:0;padding:0}
  html,body{width:1169px;height:1200px;overflow:hidden;background:var(--page)}
  body{font-family:"PT Sans",Arial,sans-serif;position:relative}

  .card{position:absolute;left:164px;width:840px;height:560px;overflow:hidden}
  .card--front{top:26px;background:linear-gradient(90deg,var(--steel-light) 0%,#a9aaad 40%,#6a6b6e 75%,#1c1c1d 100%)}
  .card--back{top:614px;background:linear-gradient(90deg,#5d5e61 0%,#3b3b3d 45%,#1f1f20 100%)}
  .card__sweep{position:absolute;inset:0;width:100%;height:100%}

  .brand{position:absolute;display:flex;align-items:center;gap:14px}
  .brand__mark{background:var(--slate);display:block}
  .brand__name{color:var(--orange);font-weight:400;white-space:nowrap}

  .card--front .brand{left:0;right:0;top:216px;justify-content:center}
  .card--front .brand__mark{width:58px;height:58px}
  .card--front .brand__name{font-size:42px}

  .card--back .brand{left:26px;top:36px}
  .card--back .brand__mark{width:80px;height:80px}
  .card--back .brand__name{font-size:34px}

  .practice__head{position:absolute;left:42px;display:flex;align-items:center;gap:8px}
  .practice__icon{width:44px;height:34px;background:var(--white);border-radius:2px;display:block}
  .practice__label{background:var(--orange);color:var(--ink);font-size:16px;padding:3px 10px;width:180px;letter-spacing:.3px}
  .practice__text{position:absolute;left:42px;width:428px;color:var(--orange);font-size:14.5px;line-height:1.38;text-align:justify;padding:12px 14px}
  .practice--injury .practice__head{top:152px}
  .practice--injury .practice__text{top:194px;height:128px;background:var(--panel);border-radius:6px}
  .practice--employment .practice__head{top:340px}
  .practice--employment .practice__text{top:392px}

  .contact-panel{position:absolute;left:42px;top:388px;width:772px;height:150px;background:var(--panel);border-radius:6px}

  .team-photo{position:absolute;left:472px;top:40px;width:340px;height:272px;background:radial-gradient(ellipse at 50% 40%,#d8d4d0 0%,#8a8680 45%,#2a2a2c 100%)}

  .slogan{position:absolute;left:462px;top:314px;width:360px;text-align:center;font-family:"EB Garamond",Georgia,serif;font-style:italic;font-size:29px;color:var(--orange)}
  .cta{position:absolute;left:466px;top:356px;width:350px;height:72px;border-radius:6px;background:linear-gradient(180deg,#f47a45,var(--orange-deep));border:2px solid #f7b394;color:var(--white);font-weight:700;font-size:19px;line-height:1.3;text-align:center;display:flex;flex-direction:column;justify-content:center;text-transform:uppercase}
  .phone{position:absolute;left:466px;top:436px;width:350px;display:flex;justify-content:center;align-items:center;gap:10px;color:var(--white);font-weight:700;font-size:29px}
  .phone svg{width:22px;height:26px}
  .address{position:absolute;left:466px;top:486px;width:350px;text-align:center;color:var(--white);font-size:13px}
  .links{position:absolute;left:466px;top:508px;width:350px;display:flex;justify-content:center;gap:12px;color:var(--white);font-size:13.5px}
  .links__sep{width:2px;background:var(--white)}
</style>
</head>
<body>

<section class="card card--front" aria-label="Flyer front">
  <svg class="card__sweep" viewBox="0 0 840 560" preserveAspectRatio="none">
    <path d="M0 370 C220 470 520 470 840 330 L840 560 L0 560 Z" fill="#5a5b5e" opacity=".75"/>
    <path d="M0 370 C220 470 520 470 840 330" fill="none" stroke="#e2e3e5" stroke-width="2" opacity=".6"/>
  </svg>
  <div class="brand">
    <span class="brand__mark"></span>
    <span class="brand__name">Marvello Quintard LLP</span>
  </div>
</section>

<section class="card card--back" aria-label="Flyer back">
  <svg class="card__sweep" viewBox="0 0 840 560" preserveAspectRatio="none">
    <path d="M0 60 L0 0 L420 0 C300 120 260 300 0 470 Z" fill="#8e8f92" opacity=".35"/>
    <path d="M60 0 L180 0 C420 180 520 330 560 560 L470 560 C420 330 300 160 60 0 Z" fill="#b4b5b8" opacity=".22"/>
    <path d="M0 560 L0 480 C300 400 600 360 840 300 L840 560 Z" fill="#4a4a4d" opacity=".5"/>
  </svg>

  <div class="brand">
    <span class="brand__mark"></span>
    <span class="brand__name">Marvello Quintard LLP</span>
  </div>

  <div class="team-photo" role="img" aria-label="Group photo of the three firm partners"></div>

  <div class="contact-panel"></div>

  <div class="practice practice--injury">
    <div class="practice__head">
      <span class="practice__icon" role="img" aria-label="Ambulance icon"></span>
      <span class="practice__label">PERSONAL INJURY</span>
    </div>
    <p class="practice__text">If you or a loved one are suffering from an injury or wrongful death caused by the careless or intentional acts of others, then you have the right to pursue compensation for your injury, out-of-pocket expenses, lost wages, emotional anguish, and more.</p>
  </div>

  <div class="practice practice--employment">
    <div class="practice__head">
      <span class="practice__icon" role="img" aria-label="Person at computer desk icon"></span>
      <span class="practice__label">EMPLOYMENT LAW</span>
    </div>
    <p class="practice__text">Our attorneys regularly represent clients in disputes involving sex, age and race discrimination, sexual harassment, retaliatory discharge, defamation, unlawful termination, breach of employment contracts, and more.</p>
  </div>

  <p class="slogan">You Speak. We Listen. They Pay.</p>
  <div class="cta"><span>Contact us</span><span>for a free consultation today!</span></div>
  <p class="phone">
    <svg viewBox="0 0 24 28" aria-hidden="true"><path d="M6 1 L10 7 L7 10 C8 15 11 19 15 21 L18 18 L23 22 L20 27 C10 26 2 16 1 5 Z" fill="#fff"/></svg>
    310.555.8143
  </p>
  <p class="address">752 W. Folbrook Lane, Suite 400 Beverly Hills, CA 90210</p>
  <p class="links"><span>Email: info@mqmlegal.example</span><span class="links__sep"></span><span>Web: www.mqmlegal.example</span></p>
</section>

</body>
</html>
```